professional business card

A Clean looking business card for a money transfer company. Our company is call Pavolex= Transfer + Send = Transcend (next level)
to show professionalism as well as some effects to show digital tech.

1 side to have position, name and address
2 side to have company name and show that we provide money exchange and cross-border money transfer

Target Market(s)

Remittance companies and high net worth individuals

Industry/Entity Type

Finance

Contact Information for Business Card

Name, address, email, title, services- money exchange and cross-border remittance

Requirements
Nice to have
• Digital age feel

```html
<!DOCTYPE html>
<html lang="en">
<head>
<meta charset="utf-8">
<title>Pavolex Business Card</title>
<link rel="stylesheet" href="https://fonts.googleapis.com/css2?family=Montserrat:wght@500;600&family=Open+Sans:wght@400;600;700&display=swap">
<style>
  :root {
    --stage: #232323;
    --navy: #263340;
    --navy-deep: #1b2631;
    --teal: #74cedc;
    --teal-dark: #0f7384;
    --white: #ffffff;
  }
  * { margin: 0; padding: 0; box-sizing: border-box; }
  html, body { width: 1200px; height: 780px; overflow: hidden; background: var(--stage); }
  .canvas {
    position: relative; width: 1200px; height: 780px;
    display: flex; align-items: center; justify-content: center; gap: 40px;
  }
  .card {
    position: relative; width: 560px; height: 320px;
    background: var(--navy); overflow: hidden;
    font-family: "Open Sans", Arial, sans-serif; color: var(--white);
  }

  /* Company side */
  .brand-large {
    position: absolute; left: 0; right: 0; top: 104px;
    display: flex; align-items: center; justify-content: center; gap: 18px;
  }
  .brand-large .dot { width: 34px; height: 34px; border-radius: 50%; background: var(--navy-deep); }
  .brand-large .name {
    font-family: "Montserrat", Arial, sans-serif; font-weight: 600;
    font-size: 62px; letter-spacing: 2px; color: var(--navy-deep);
  }
  .services {
    position: absolute; left: 0; right: 0; bottom: 46px;
    display: flex; align-items: center; justify-content: center; gap: 10px;
    font-size: 15px;
  }
  .services .label { color: var(--teal); letter-spacing: 0.5px; }
  .services .bullet { width: 8px; height: 8px; border-radius: 50%; background: var(--teal); }

  /* Personal side */
  .card-shape { position: absolute; inset: 0; }
  .brand-small {
    position: absolute; left: 32px; top: 34px;
    display: flex; align-items: center; gap: 12px;
  }
  .brand-small .dot { width: 24px; height: 24px; border-radius: 50%; background: var(--teal); }
  .brand-small .name {
    font-family: "Montserrat", Arial, sans-serif; font-weight: 600;
    font-size: 30px; letter-spacing: 1px; color: var(--white);
  }
  .person { position: absolute; left: 32px; top: 108px; padding-left: 20px; }
  .person::before {
    content: ""; position: absolute; left: 0; top: 4px; width: 9px; height: 52px; background: var(--teal);
  }
  .person .full-name { font-size: 27px; font-weight: 700; line-height: 1.1; }
  .person .first { color: var(--teal); }
  .person .title { font-size: 15px; font-weight: 600; margin-top: 4px; }
  .address { position: absolute; left: 72px; top: 186px; font-size: 14px; line-height: 1.4; }
  .contacts { position: absolute; left: 60px; top: 236px; list-style: none; font-size: 14px; line-height: 1.5; }
  .contacts li { display: flex; align-items: center; gap: 8px; }
  .contacts svg { width: 13px; height: 13px; flex: none; }
</style>
</head>
<body>
<main class="canvas">

  <section class="card card--company" aria-label="Company side">
    <div class="brand-large">
      <span class="dot"></span>
      <span class="name">PAVOLEX</span>
    </div>
    <p class="services">
      <span class="label">SERVICES</span>
      <span class="bullet"></span>
      <span>Money exchange</span>
      <span class="bullet"></span>
      <span>Cross-border remittance</span>
    </p>
  </section>

  <section class="card card--contact" aria-label="Contact side">
    <svg class="card-shape" viewBox="0 0 560 320" preserveAspectRatio="none">
      <path d="M312 0 C268 110 318 240 430 320 L560 320 L560 0 Z" fill="var(--teal)"/>
      <path d="M330 0 C290 110 336 236 436 320 L560 320 L560 0 Z" fill="var(--teal-dark)"/>
      <path d="M334 0 C296 110 340 236 440 320 L560 320 L560 0 Z" fill="var(--white)"/>
    </svg>

    <div class="brand-small">
      <span class="dot"></span>
      <span class="name">PAVOLEX</span>
    </div>

    <div class="person">
      <p class="full-name"><span class="first">Marta</span> Velinska</p>
      <p class="title">Managing Director</p>
    </div>

    <p class="address">418 Harlow Ave. Suite 120<br>Denton, TX 76201</p>

    <ul class="contacts">
      <li>
        <svg viewBox="0 0 16 16"><path d="M4 1 L6.5 4 L5 6 C6 8.5 7.5 10 10 11 L12 9.5 L15 12 L13 15 C7 14.5 1.5 9 1 3 Z" fill="var(--teal)"/></svg>
        (555) 014-3820
      </li>
      <li>
        <svg viewBox="0 0 16 16"><rect x="1" y="3" width="14" height="10" rx="1" fill="var(--teal)"/><path d="M1.5 3.5 L8 9 L14.5 3.5" fill="none" stroke="var(--navy)" stroke-width="1.3"/></svg>
        hello@pavolex.example
      </li>
      <li>
        <svg viewBox="0 0 16 16"><circle cx="8" cy="8" r="7" fill="var(--teal)"/><path d="M1 8 H15 M8 1 C4 5 4 11 8 15 M8 1 C12 5 12 11 8 15" fill="none" stroke="var(--navy)" stroke-width="1"/></svg>
        www.pavolex.example
      </li>
    </ul>
  </section>

</main>
</body>
</html>
```